Trade show banner design

We need an 8 x 2.5' and a 6 x 2.5' banner for trade shows. We would like you to use the last book cover design you submitted with the woman on the right of the banner using the catchphrase underneath and the couple on the left of the banner with the catchphrase underneath. We prefer the font under the couple, so please use this for both. In the middle at the top will be the company logo and www.talesfromkin.com with our phone numbers underneath that. If you think the logo would look nicer in the middle please feel free to play with the balance.
Also, the Tales from Kin will not be necessary above the woman's head.
THANK YOU!!!!!!!!
717-382-5061 and 844-4TALEKIN.

Industry/Entity Type

Trade

```html
<!DOCTYPE html>
<html lang="en">
<head>
<meta charset="utf-8">
<title>Tales from Kin – Trade Show Banner 6 x 2.5 ft</title>
<link rel="stylesheet" href="https://fonts.googleapis.com/css2?family=EB+Garamond:ital,wght@1,500;1,600&display=swap">
<style>
  :root {
    --page: #ffffff;
    --ink: #111111;
    --banner-edge: #f7a083;
    --banner-glow: #fcc0a6;
    --brand: #9a4a22;
    --frame-gold: #f3c98a;
    --rule: #b99488;
    --ornament-dark: #6e4a40;
    --scroll-warm: #c7651f;
    --scroll-deep: #8a3a14;
    --sunset-top: #f0c56a;
    --sunset-mid: #c5702a;
    --sunset-low: #1c0a04;
    --study-light: #c9a17a;
    --study-mid: #6b4026;
    --study-dark: #2e1a10;
  }
  * { margin: 0; padding: 0; box-sizing: border-box; }
  html, body {
    width: 1200px; height: 900px; overflow: hidden;
    background: var(--page);
    font-family: "EB Garamond", Georgia, serif;
    font-style: italic;
    font-variant-numeric: lining-nums;
    color: var(--ink);
  }
  .canvas { position: relative; width: 1200px; height: 900px; }

  .size-label {
    position: absolute; left: 232px; top: 118px;
    font-size: 80px; font-weight: 500; letter-spacing: 5px; word-spacing: 10px; line-height: 1;
    white-space: nowrap;
  }

  .banner {
    position: absolute; left: 0; top: 323px; width: 1200px; height: 503px;
    background: radial-gradient(ellipse 40% 55% at 50% 50%, var(--banner-glow), var(--banner-edge) 100%);
    overflow: hidden;
  }

  .corner-flourish {
    position: absolute; top: 6px; width: 86px; height: 84px;
    opacity: .8;
  }
  .corner-flourish.left {
    left: 8px;
    background: radial-gradient(ellipse 80% 80% at 20% 20%, var(--ornament-dark) 0%, rgba(110,74,64,.55) 45%, rgba(110,74,64,0) 75%);
  }
  .corner-flourish.right {
    right: 8px;
    background: radial-gradient(ellipse 80% 80% at 80% 20%, var(--ornament-dark) 0%, rgba(110,74,64,.55) 45%, rgba(110,74,64,0) 75%);
  }

  .photo {
    position: absolute; border-radius: 50%;
    border: 2px solid var(--frame-gold);
    box-shadow: 0 0 10px 4px rgba(255, 236, 200, .75);
  }
  .photo.couple {
    left: 27px; top: 22px; width: 304px; height: 416px;
    background: linear-gradient(180deg, var(--sunset-top) 0%, #e9a645 35%, var(--sunset-mid) 50%, #4a1d0a 60%, var(--sunset-low) 72%, var(--sunset-low) 100%);
  }
  .photo.writer {
    left: 882px; top: 22px; width: 283px; height: 413px;
    background: radial-gradient(ellipse 70% 60% at 65% 40%, var(--study-light), var(--study-mid) 60%, var(--study-dark) 100%);
  }

  .web-address {
    position: absolute; left: 350px; top: 16px; width: 506px;
    font-size: 37px; font-weight: 500; letter-spacing: 3px; text-align: center; white-space: nowrap;
  }
  .phones {
    position: absolute; left: 320px; top: 68px; width: 530px;
    display: flex; justify-content: center; gap: 20px;
    font-size: 25px; font-weight: 500; letter-spacing: 2px; white-space: nowrap;
  }
  .phones span { display: inline-flex; align-items: center; gap: 8px; }
  .phones svg { width: 17px; height: 17px; }

  .scroll-frame {
    position: absolute; left: 352px; top: 125px; width: 510px; height: 255px;
    border-radius: 50%;
    background: radial-gradient(ellipse 50% 50% at 50% 50%, rgba(252,196,170,.0) 55%, rgba(199,101,31,.35) 72%, rgba(138,58,20,.45) 82%, rgba(199,101,31,.15) 92%, rgba(199,101,31,0) 100%);
  }

  .brand-name {
    position: absolute; left: 352px; top: 218px; width: 510px;
    text-align: center; font-size: 54px; font-weight: 600; line-height: 1;
    color: var(--brand); letter-spacing: 1px; white-space: nowrap;
  }

  .divider {
    position: absolute; left: 362px; top: 417px; width: 466px; height: 1px;
    background: var(--rule);
  }
  .divider-ornament {
    position: absolute; left: 435px; top: 407px; width: 320px; height: 22px;
    border-radius: 11px;
    background: linear-gradient(90deg, rgba(185,148,136,0), rgba(160,120,110,.7) 20%, rgba(200,170,160,.8) 50%, rgba(160,120,110,.7) 80%, rgba(185,148,136,0));
  }

  .tagline { position: absolute; font-weight: 500; line-height: 1; white-space: nowrap; }
  .tagline.left { left: 14px; top: 452px; font-size: 28px; letter-spacing: 1.5px; }
  .tagline.right {
    left: 826px; top: 450px; width: 366px; text-align: center;
    font-size: 22px; letter-spacing: 1.5px; line-height: 1.02; white-space: normal;
  }
</style>
</head>
<body>
<main class="canvas">
  <p class="size-label">size 6 x 2.5 feet</p>

  <section class="banner" aria-label="Tales from Kin trade show banner">
    <div class="corner-flourish left" role="img" aria-label="Decorative scrollwork corner flourish"></div>
    <div class="corner-flourish right" role="img" aria-label="Decorative scrollwork corner flourish"></div>

    <div class="photo couple" role="img" aria-label="Photo of an elderly couple walking along a beach at sunset"></div>
    <div class="photo writer" role="img" aria-label="Photo of an elderly woman writing at a wooden desk by lamplight"></div>

    <p class="web-address">www.talesfromkin.com</p>
    <p class="phones">
      <span><svg viewBox="0 0 16 16" aria-hidden="true"><ellipse cx="8" cy="7" rx="7" ry="5.5" fill="#111"/><path d="M5 11 L4 15 L9 12 Z" fill="#111"/></svg>717-382-5061</span>
      <span><svg viewBox="0 0 16 16" aria-hidden="true"><ellipse cx="8" cy="7" rx="7" ry="5.5" fill="#111"/><path d="M5 11 L4 15 L9 12 Z" fill="#111"/></svg>844-4TALEKIN</span>
    </p>

    <div class="scroll-frame" role="img" aria-label="Ornamental gold scrollwork frame around the company name"></div>
    <p class="brand-name">Tales from Kin</p>

    <div class="divider"></div>
    <div class="divider-ornament" role="img" aria-label="Decorative scroll ornament on the divider line"></div>

    <p class="tagline left">When a genealogy doesn't say enough...</p>
    <p class="tagline right">Every life legacy is a gift to be treasured by the next generation</p>
  </section>
</main>
</body>
</html>
```